I need a design with just the number 24. must be in blue color (royal blue) should be large enough for people see must be in the center of page. Place a nice border around the page.

• Number 24 in Royal blue color

```html
<!DOCTYPE html>
<html lang="en">
<head>
<meta charset="utf-8">
<title>24</title>
<link rel="stylesheet" href="https://fonts.googleapis.com/css2?family=Playfair+Display:wght@700&display=swap">
<style>
  :root {
    --paper: #ffffff;
    --night: #0c0c0d;
    --royal: #0033a0;
    --royal-light: #1a5fd0;
    --neon: #1aa6ff;
  }
  html, body {
    margin: 0;
    padding: 0;
    width: 828px;
    height: 1200px;
    overflow: hidden;
    background: var(--paper);
  }
  .poster {
    position: relative;
    width: 828px;
    height: 1200px;
  }
  .poster__art {
    position: absolute;
    inset: 0;
    display: block;
    width: 828px;
    height: 1200px;
  }
  .poster__edge { fill: var(--paper); }
  .poster__field { fill: var(--night); }
  .neon-frame {
    fill: none;
    stroke: var(--neon);
    stroke-width: 5;
    filter: url(#glow);
  }
  .numeral {
    position: absolute;
    left: 0;
    top: 0;
    width: 828px;
    height: 1200px;
    display: flex;
    align-items: center;
    justify-content: center;
    margin: 0;
    font-family: "Playfair Display", Georgia, serif;
    font-weight: 700;
    font-size: 520px;
    line-height: 1;
    letter-spacing: -0.04em;
    color: var(--royal);
    text-shadow: 0 12px 24px rgba(0, 0, 0, 0.7);
    transform: translate(2px, -10px) scaleY(1.5);
  }
</style>
</head>
<body>
<div class="poster">
  <svg class="poster__art" viewBox="92 125 1398 1975" preserveAspectRatio="none" xmlns="http://www.w3.org/2000/svg">
    <defs>
      <radialGradient id="tech-glow" cx="790" cy="1130" r="640" gradientUnits="userSpaceOnUse">
        <stop offset="0" stop-color="#8a8a8a"/>
        <stop offset="0.3" stop-color="#4a4a4a"/>
        <stop offset="0.7" stop-color="#1c1c1c"/>
        <stop offset="1" stop-color="#0c0c0d"/>
      </radialGradient>
      <filter id="glow" x="-10%" y="-10%" width="120%" height="120%">
        <feGaussianBlur stdDeviation="6" result="blur"/>
        <feMerge>
          <feMergeNode in="blur"/>
          <feMergeNode in="SourceGraphic"/>
        </feMerge>
      </filter>
    </defs>

    <rect class="poster__edge" x="92" y="125" width="1398" height="1975"/>
    <rect class="poster__field" x="106" y="138" width="1370" height="1950"/>
    <rect x="106" y="138" width="1370" height="1950" fill="url(#tech-glow)" role="img" aria-label="Glowing circular technology dial with faint binary code behind the number"/>

    <path class="neon-frame" d="M632 198 H166 V2040 H992 V1790"/>
    <path class="neon-frame" d="M676 420 V198 H1422 V2045 H1205 V1790"/>
  </svg>

  <h1 class="numeral">24</h1>
</div>
</body>
</html>
```